Quiet Rivers Under Open Skies

This is the sequel to a book published 40 years ago that serves as the base benchmark for progress in the field of environmental management in Queensland. The book describes the outcomes of long-term field programs in environmental management across the large State of Queensland in Australia. No book of this type has been published in Australia previously. The book will be published by Harbourline Author Press, with limp cover.

Target Market(s)

Global audience via Shopvale.com

Industry/Entity Type

Environment

Other font styles liked:
• Palatino (This is text and presumably should be cover type)

Requirements
Must have
• Colour front cover, back cover and spine sized according to the requirements of Harbourline Author Press 8.5" X 11" (215.9mm X 279.4 mm) template with 0.68" spine width (17.16mm) (spine width based on current estimation of page number) - as per .jpeg files submitted. Some amendments have been necessary based on excellent designs so far submitted (see two new files).
Designs to date have been excellent and have led to a title change that can either readily be changed on the design finally chosen or considered by those designers still to submit.
Nice to have
• A professional appearance, in keeping with the semi-technical nature of the narrative. A spine as distinctive as the first edition of Saltbush Horizons (see attached file). The text on the back cover may need minor editing, probably at the time that endorsements are added (after first proof copy).

```html
<!DOCTYPE html>
<html lang="en">
<head>
<meta charset="utf-8">
<title>Quiet Rivers Under Open Skies — Cover</title>
<link rel="stylesheet" href="https://fonts.googleapis.com/css2?family=Crimson+Text:ital,wght@0,400;0,600;1,400&family=Gelasio:ital,wght@0,400;0,600;1,400;1,500&display=swap">
<style>
  :root {
    --paper: #dde4d2;
    --ink: #141414;
    --navy: #1b2033;
    --rule: #a9ada2;
    --benchmark-green: #1f9a57;
    --book-green: #11804a;
    --maroon: #5a1028;
  }
  html, body { margin: 0; padding: 0; overflow: hidden; background: var(--paper); }
  .cover {
    position: relative; width: 1200px; height: 747px; overflow: hidden;
    background: var(--paper); color: var(--ink);
    font-family: "Crimson Text", "Palatino Linotype", serif;
  }
  .abs { position: absolute; }

  /* Back cover */
  .first-edition {
    left: 50px; top: 58px; width: 186px; height: 239px;
    background: var(--book-green); box-sizing: border-box; padding: 6px 8px;
    color: #f4f1e6; text-align: center; font-family: "Gelasio", Georgia, serif;
  }
  .first-edition .series { font-size: 11px; border-bottom: 1px solid #e8e4d6; padding-bottom: 2px; }
  .first-edition .book-title { font-size: 16px; font-weight: 600; line-height: 15px; margin-top: 3px; }
  .first-edition .editor { font-size: 6px; border-top: 1px solid #e8e4d6; margin-top: 4px; padding-top: 3px; }
  .first-edition .book-photo {
    margin: 5px auto 0; width: 164px; height: 146px; border: 1px solid #e8e4d6;
    background: linear-gradient(160deg, #5e5a4c, #8c7f6a 50%, #3b3a2e);
  }
  .benchmark-caption {
    left: 40px; top: 307px; width: 206px; text-align: center;
    color: var(--benchmark-green); font-size: 13px; line-height: 15.5px; font-weight: 600;
    font-family: "Gelasio", Georgia, serif;
  }
  .back-divider { left: 254px; top: 55px; width: 1px; height: 282px; background: var(--rule); }
  .blurb {
    left: 278px; top: 51px; margin: 0; white-space: nowrap;
    font-style: italic; font-size: 14.5px; line-height: 19.4px;
  }
  .author-photo {
    left: 52px; top: 362px; width: 139px; height: 162px; box-sizing: border-box;
    border: 2px solid #fff; background: linear-gradient(170deg, #5f6e74, #a58f7d 45%, #6b5e45);
  }
  .author-bio {
    left: 216px; top: 358px; margin: 0; white-space: nowrap;
    font-size: 15px; line-height: 20.6px;
  }
  .publisher-mark { left: 150px; top: 672px; display: flex; align-items: center; gap: 8px; }
  .publisher-mark .dot { width: 10px; height: 10px; border-radius: 50%; background: var(--maroon); }
  .publisher-mark .name { font-size: 11px; line-height: 11px; color: var(--maroon); }
  .isbn-space { left: 356px; top: 620px; width: 167px; height: 103px; background: #fff; }
  .base-rule { left: 0; top: 673px; width: 1200px; height: 1px; background: var(--rule); }

  /* Spine */
  .spine-title {
    left: 600px; top: 147px; transform-origin: 0 0; transform: rotate(90deg) translateY(-50%);
    white-space: nowrap; font-family: "Gelasio", Georgia, serif;
    font-style: italic; font-size: 34px; line-height: 38px;
  }
  .spine-author {
    left: 600px; top: 680px; transform-origin: 0 0; transform: rotate(90deg) translateY(-50%);
    white-space: nowrap; font-family: "Gelasio", Georgia, serif;
    font-style: italic; font-size: 14px; line-height: 18px;
  }

  /* Front cover */
  .mosaic .tile { position: absolute; }
  .front-title {
    left: 720px; top: 502px; width: 400px; margin: 0; text-align: center;
    font-family: "Gelasio", Georgia, serif;
    font-style: italic; font-weight: 400; font-size: 41px; line-height: 47px;
  }
  .front-subtitle {
    left: 700px; top: 619px; width: 440px; margin: 0; text-align: center;
    font-family: "Gelasio", Georgia, serif;
    font-style: italic; font-weight: 500; font-size: 19px; color: var(--navy);
  }
  .front-author {
    left: 720px; top: 686px; width: 400px; margin: 0; text-align: center;
    font-family: "Gelasio", Georgia, serif;
    font-style: italic; font-size: 35px; line-height: 42px;
  }
</style>
</head>
<body>
<main class="cover">
  <!-- Back cover -->
  <div class="abs first-edition">
    <div class="series">Saltbush Horizons</div>
    <div class="book-title">A Natural History of the North</div>
    <div class="editor">Edited by M.J. Ellery</div>
    <div class="book-photo" role="img" aria-label="Photograph of a small furry marsupial perched on a branch"></div>
  </div>
  <div class="abs benchmark-caption">THE BENCHMARK BOOK,<br>WRITTEN 40 YEARS AGO.</div>
  <div class="abs back-divider"></div>
  <p class="abs blurb">Long-term research programs across the<br>large and diverse Australian State of<br>Queensland show that environmental<br>legislation needs to be underpinned by<br>another process – the environmental<br>narrative.&nbsp; With this instrument, the<br>current operational tools of the national<br>park, threatened species list and<br>environmental impact statement are<br>reinforced by another toolkit of modern<br>techniques based on ecological design.<br>Crafted narratives can then inspire the<br>community to deliver effective<br>conservation of this remarkable<br>landscape.</p>
  <div class="abs author-photo" role="img" aria-label="Portrait photograph of the author"></div>
  <p class="abs author-bio">Dr Martin Ellery AM is one of Australia’s<br>longest serving environmental scientists<br>(Certified Environmental Practitioner Reg.#001<br>of the Institute of Regional Ecology).&nbsp; His<br>field work has taken him deep into all of the<br>natural ecosystems of Queensland – and to<br>many other parts of the world on their behalf.</p>
  <div class="abs publisher-mark"><span class="dot"></span><span class="name">Coastal Range<br>Institute</span></div>
  <div class="abs isbn-space"></div>
  <div class="abs base-rule"></div>

  <!-- Spine -->
  <div class="abs spine-title">Quiet Rivers Under Open Skies</div>
  <div class="abs spine-author">Martin E.</div>

  <!-- Front cover photo mosaic -->
  <div class="mosaic">
    <div class="tile" style="left:622px;top:0;width:106px;height:57px;background:linear-gradient(#8fa9b8,#4f6b5a)" role="img" aria-label="Photograph of rainforest and ferns"></div>
    <div class="tile" style="left:576px;top:57px;width:152px;height:60px;background:linear-gradient(#3f6a3a,#2c4a24)" role="img" aria-label="Rainforest ferns, continued"></div>
    <div class="tile" style="left:728px;top:0;width:124px;height:117px;background:linear-gradient(#5d8fd0 0%,#a9c3e0 35%,#e06a26 55%,#c84816)" role="img" aria-label="Photograph of a red desert dune under a blue sky"></div>
    <div class="tile" style="left:853px;top:0;width:116px;height:117px;background:linear-gradient(140deg,#6f7a5a,#9a8a72)" role="img" aria-label="Photograph of kangaroos"></div>
    <div class="tile" style="left:970px;top:0;width:115px;height:117px;background:linear-gradient(140deg,#3d4a2f,#1c1f16 55%,#c8a020)" role="img" aria-label="Photograph of a black and gold bowerbird"></div>

    <div class="tile" style="left:622px;top:117px;width:112px;height:56px;background:linear-gradient(#4e5b43,#2f3a2a)" role="img" aria-label="Photograph of a glider among flowers"></div>
    <div class="tile" style="left:677px;top:173px;width:57px;height:61px;background:linear-gradient(#3a4a35,#c9a32a)" role="img" aria-label="Glider photograph, continued"></div>
    <div class="tile" style="left:734px;top:117px;width:117px;height:117px;background:linear-gradient(140deg,#1d5a36,#1a1a1a 50%,#c9b52a)" role="img" aria-label="Photograph of a butterfly on yellow blossom"></div>
    <div class="tile" style="left:851px;top:117px;width:117px;height:117px;background:linear-gradient(140deg,#121212,#7a3028 55%,#1b2a18)" role="img" aria-label="Photograph of a red orchid"></div>
    <div class="tile" style="left:968px;top:117px;width:177px;height:117px;background:linear-gradient(140deg,#3d5a2c,#a08a60 50%,#2a4a22)" role="img" aria-label="Photograph of a waterfall in a gorge"></div>

    <div class="tile" style="left:737px;top:234px;width:114px;height:115px;background:linear-gradient(140deg,#2a2c30,#5a6470 50%,#1f2227)" role="img" aria-label="Photograph of a fish among rocks"></div>
    <div class="tile" style="left:851px;top:234px;width:116px;height:115px;background:linear-gradient(140deg,#8c8e88,#3a3d36 50%,#b8b8b0)" role="img" aria-label="Photograph of a sea turtle on sand"></div>
    <div class="tile" style="left:967px;top:234px;width:117px;height:115px;background:linear-gradient(#3b5c66,#2e4a2c)" role="img" aria-label="Aerial photograph of forested escarpment"></div>
    <div class="tile" style="left:1084px;top:234px;width:116px;height:115px;background:linear-gradient(#1a4c8c,#3f9ec8 55%,#1a4a84)" role="img" aria-label="Aerial photograph of a coral reef island"></div>

    <div class="tile" style="left:677px;top:349px;width:59px;height:58px;background:linear-gradient(#b8a070,#8a7045)" role="img" aria-label="Photograph of a bilby"></div>
    <div class="tile" style="left:623px;top:407px;width:113px;height:58px;background:linear-gradient(#a08a60,#b86a34)" role="img" aria-label="Bilby photograph, continued"></div>
    <div class="tile" style="left:736px;top:349px;width:115px;height:116px;background:linear-gradient(#2d3a26,#3a3530 60%,#8a6a45)" role="img" aria-label="Photograph of a wombat"></div>
    <div class="tile" style="left:851px;top:349px;width:116px;height:116px;background:linear-gradient(140deg,#4a6a3a,#9aa0a2 50%,#3a4a2e)" role="img" aria-label="Photograph of a koala in a tree"></div>
    <div class="tile" style="left:967px;top:349px;width:113px;height:116px;background:linear-gradient(#4c9ac4,#1c5a8a 50%,#0c2a4a)" role="img" aria-label="Photograph of a turtle swimming underwater"></div>
    <div class="tile" style="left:1080px;top:349px;width:64px;height:58px;background:#0e1622"></div>
  </div>

  <h1 class="abs front-title">Quiet Rivers<br>Under Open Skies</h1>
  <p class="abs front-subtitle">Conserving Queensland’s Natural Environment</p>
  <p class="abs front-author">Martin Ellery</p>
</main>
</body>
</html>
```